Label template request for Pellow & Co

Project Overview:We are a handmade bath and body brand looking for an experienced packaging/label designer to create a cohesive label system for our products.

Our brand style is playful, clean, modern, bold, and slightly magical.

Scope of Work:
1. Label Template SystemDesign cohesive, print-ready templates for:
Bar soap wraps
Jar labels (scrubs, salts, creams)
Bottle labels (sprays, oils)
Small product tags
Generic shopping bag labels and stickers for shipped items.

Templates must be editable (preferably Canva-compatible) so we can update scents and product names.

Deliverables:
Print-ready files (PDF + source files)
Editable templates
Font and color specs

Ideal Candidate:
Experience with packaging/label design
Familiar with print requirements
Able to design scalable template systems
Strong portfolio of product branding work

To Apply, Please Include:

Portfolio (packaging examples preferred)
Estimated timeline
Pricing for full project
Confirmation you can provide Canva-editable files

We are looking for someone who can help create a polished, cohesive visual system for a growing product brand.

Target Market(s)

All ages, modern urban families, wide range demographics and ethnicities.

Industry/Entity Type

Soap, lotions, cosmetics

Font styles to use
Serif

Colors
FFC000
F8CF3A
FAE287
FDF2CF
FEFAEE
F0912C
F2A743
F7CA91
FBE8D2
FDF5EE
E54698
E96AAD
F1A4CE
F9D9EA
FCEFF6

Requirements
Must have
• Somewhat similar concept to example photos given, but would like you to bring your own creative ideas based on it.
Nice to have
• Water elements (flowing movement), mystical elements
Should not have
• Apothecary, farmhouse or floral style, bubbles, elegant or ornate script font

```html
<!DOCTYPE html>
<html lang="en">
<head>
<meta charset="utf-8">
<title>Pellow &amp; Co – Label System</title>
<link rel="stylesheet" href="https://fonts.googleapis.com/css2?family=Poppins:wght@600&family=Permanent+Marker&display=swap">
<style>
  :root {
    --canvas: #ffffff;
    --ink-light: #ffffff;
    --paper: #efe2cc;
    --lavender-light: #d9a8ee;
    --lavender: #b65ee0;
    --lavender-deep: #9a3ddb;
    --mauve: #b07ab8;
    --coral: #ee8a6c;
    --coral-deep: #e36d55;
    --blush: #f3b6b0;
    --dusk: #a596cc;
  }
  * { margin: 0; padding: 0; box-sizing: border-box; }
  html, body { width: 1200px; height: 647px; overflow: hidden; background: var(--canvas); }
  .canvas { position: relative; width: 1200px; height: 647px; }

  .soap-wrap {
    position: absolute; left: 179px; top: 113px; width: 470px; height: 425px;
    overflow: hidden; color: var(--ink-light);
  }
  .jar-label {
    position: absolute; left: 743px; top: 195px; width: 286px; height: 286px;
    border-radius: 50%; overflow: hidden; color: var(--ink-light);
  }
  .artwork { position: absolute; inset: 0; width: 100%; height: 100%; }

  .text { position: absolute; white-space: nowrap; line-height: 1; }
  .brand-name { font-family: "Poppins", sans-serif; font-weight: 600; letter-spacing: 0.04em; }
  .scent-name { font-family: "Permanent Marker", cursive; font-weight: 400; transform: skewX(-8deg); }
  .product-type, .net-weight { font-family: "Poppins", sans-serif; font-weight: 600; line-height: 0.95; }

  .soap-wrap .brand-name { left: 0; width: 470px; text-align: center; top: 216px; font-size: 30px; }
  .soap-wrap .scent-name { left: 0; width: 470px; text-align: center; top: 295px; font-size: 40px; letter-spacing: 0.03em; }
  .soap-wrap .product-type { left: 48px; top: 370px; font-size: 19px; letter-spacing: 0.08em; text-align: center; }
  .soap-wrap .net-weight { right: 47px; top: 382px; font-size: 12px; letter-spacing: 0.06em; }

  .jar-label .brand-name { left: 0; width: 286px; text-align: center; top: 46px; font-size: 18px; }
  .jar-label .scent-name { left: 0; width: 286px; text-align: center; top: 108px; font-size: 36px; line-height: 1.15; letter-spacing: 0.03em; }
  .jar-label .product-type { left: 63px; top: 226px; font-size: 11px; letter-spacing: 0.04em; }
  .jar-label .net-weight { left: 157px; top: 228px; font-size: 8.5px; letter-spacing: 0.03em; }
</style>
</head>
<body>
<main class="canvas">

  <section class="soap-wrap">
    <svg class="artwork" role="img" aria-label="Watercolour lavender clouds rising over textured cream paper" viewBox="0 0 470 425" preserveAspectRatio="none">
      <defs>
        <linearGradient id="soapWash" x1="0" y1="0" x2="0.15" y2="1">
          <stop offset="0" stop-color="var(--paper)"/>
          <stop offset="0.12" stop-color="var(--paper)"/>
          <stop offset="0.3" stop-color="var(--mauve)"/>
          <stop offset="0.5" stop-color="var(--lavender-deep)"/>
          <stop offset="0.8" stop-color="var(--lavender-light)"/>
          <stop offset="1" stop-color="var(--lavender)"/>
        </linearGradient>
      </defs>
      <rect width="470" height="425" fill="url(#soapWash)"/>
    </svg>
    <p class="text brand-name">PELLOW &amp; CO</p>
    <h2 class="text scent-name">LAVENDER + SAGE</h2>
    <p class="text product-type">ARTISAN<br>SOAP</p>
    <p class="text net-weight">NET WT. 4.5oz / 127g</p>
  </section>

  <section class="jar-label">
    <svg class="artwork" role="img" aria-label="Watercolour wash of coral, blush and soft violet clouds" viewBox="0 0 286 286">
      <defs>
        <radialGradient id="jarWash" cx="0.5" cy="0.5" r="0.6">
          <stop offset="0" stop-color="var(--coral-deep)"/>
          <stop offset="0.45" stop-color="var(--coral)"/>
          <stop offset="0.75" stop-color="var(--blush)"/>
          <stop offset="1" stop-color="var(--dusk)"/>
        </radialGradient>
      </defs>
      <rect width="286" height="286" fill="url(#jarWash)"/>
    </svg>
    <p class="text brand-name">PELLOW &amp; CO</p>
    <h2 class="text scent-name">GERANIUM<br>+ JASMIN</h2>
    <p class="text product-type">BODY<br>BUTTER</p>
    <p class="text net-weight">NET WT.<br>5oz / 147ml</p>
  </section>

</main>
</body>
</html>
```